minimalist website update needed, have wireframes

*Please start by making a design of the My Accounts page. If the overall template is correct, we can expand from there. Will give fast feedback.*

Financial services company (think online banking) is doing a complete website overhaul. We are going for the easiest, simplest possible user experience. We have the entire site mocked up in wireframes, but need a designer to make the final design drafts using photoshop or similar, then it needs to be coded into HTML/CSS.

*Current website*
https://venlotrix.com/

*New website*
+ minimalist
+ white label of https://dubrapurse.org
+ skinning dubrapurse to be Venlotrix branded, and targeted at beginners
+ wireframes for customized pages are attached
+ Landing page design is open. Please suggest one for bonus points!

Notes on the wireframes:
Open to rearranging the header content and menus.
Footer content is very rough. Just need to have a nice placeholder.
Needs social media icons
Needs language selector
My Accounts content is very rough. We want to use this area as a modular dashboard.
App Store is really just links to Bitcoin websites. These help users find useful and fun places to spend their money.

*Branding?*
As part of the process, our branding may need an update. Orange is currently our primary color, and it doesn't match well with the new, simplistic layout. We're willing to explore changes to the brand, if it works better with the new design.

Current visual identity guide is attached.
Updates

Project Deadline Extended
Reason: It seems for this many pages, it is better to leave more time. First we have to get the template right, then content elements, then HTML/CSS. I underestimated the complexity, forgive me for the modification.

Target Market(s)

People who make online purchases, or send money online.

Industry/Entity Type

Financial

Coding

Coded - Design and coding required

Number of Pages Required

5+ page

Requirements
Must have
• Pretty versions of the attached wireframes in HTML
Nice to have
• Landing page

```html
<!DOCTYPE html>
<html lang="en">
<head>
<meta charset="utf-8">
<title>Venlotrix – Add Account</title>
<link href="https://fonts.googleapis.com/css2?family=Open+Sans:wght@400;600;700&display=swap" rel="stylesheet">
<style>
:root{
  --green:#74bfa5;
  --green-foot:#78c2a8;
  --green-dark:#5fa88e;
  --orange:#e97a37;
  --page:#f5f5f5;
  --white:#ffffff;
  --text:#555a5c;
  --muted:#6b6f70;
  --heading:#3f4446;
  --link:#1e3a78;
  --rule:#e3e3e3;
}
*{box-sizing:border-box;margin:0;padding:0}
html,body{width:1200px;height:1163px;overflow:hidden}
body{position:relative;font-family:"Open Sans",Arial,sans-serif;background:var(--page);color:var(--text)}
.abs{position:absolute}
a{color:inherit;text-decoration:none}

/* sidebar */
.sidebar{left:0;top:0;width:270px;height:885px;background:var(--white);box-shadow:2px 0 3px rgba(0,0,0,.05)}
.brand{position:absolute;left:0;top:0;width:270px;height:225px;display:flex;flex-direction:column;align-items:center;justify-content:center;gap:10px}
.brand-dot{width:58px;height:58px;border-radius:50%;background:var(--orange)}
.brand-name{font-weight:700;font-size:22px;letter-spacing:5px;color:var(--orange)}
.menu{position:absolute;top:225px;left:0;width:268px;list-style:none}
.menu li{height:64px;border-bottom:1px solid var(--rule);display:flex;align-items:center;padding-left:61px;font-size:16px;color:var(--heading);position:relative}
.menu li svg{position:absolute;left:32px;top:50%;transform:translateY(-50%)}
.menu li.active{background:#f7f7f7;border-left:3px solid var(--orange);padding-left:58px}
.menu li.active svg{left:29px}

/* top bar */
.topbar{left:270px;top:0;width:930px;height:64px;background:var(--green);color:var(--white)}
.email{left:27px;top:19px;font-size:16px}
.balance{left:180px;top:17px;width:204px;height:29px;background:var(--white);color:#777;font-size:13px;line-height:29px;padding-left:9px}
.balance .caret{position:absolute;right:0;top:0;width:27px;height:29px;background:var(--orange);display:flex;align-items:center;justify-content:center}
.nav{top:24px;font-size:14px;font-weight:600}
.signout{left:780px;top:17px;width:134px;height:28px;background:var(--orange);font-size:14px;font-weight:600;display:flex;align-items:center;justify-content:center;gap:8px}

/* title bar */
.titlebar{left:270px;top:64px;width:930px;height:54px;background:var(--white);box-shadow:0 1px 2px rgba(0,0,0,.05)}
.titlebar h1{text-align:center;font-weight:400;font-size:22px;color:var(--orange);line-height:54px}
.help{right:18px;top:17px;width:19px;height:19px;border-radius:50%;background:var(--orange);color:var(--white);font-size:13px;font-weight:700;text-align:center;line-height:19px}

/* steps */
.step-num{width:34px;height:34px;border-radius:50%;background:var(--orange);color:var(--white);font-size:16px;text-align:center;line-height:34px}
.step-title{font-size:17.5px;font-weight:600;color:var(--heading)}
.copy{font-size:13px;line-height:19.5px;color:var(--muted)}
.copy u{color:var(--link);text-decoration:underline}
.panel{background:var(--white)}
.info{font-size:13px;line-height:21.2px;padding:27px 24px 0 29px}
.option-bar{background:var(--orange);color:var(--white);font-size:16px;padding-left:22px;line-height:36px}
.options{font-size:13.5px;line-height:21px;color:var(--muted);padding:17px 18px}
.check{width:15px;height:15px;border:1px solid #c9c9c9;background:var(--white)}
.btn{background:var(--green);color:var(--white);font-size:16px;font-weight:600;text-align:center;line-height:37px;border-bottom:3px solid var(--green-dark)}

/* footer */
.footer{left:0;top:885px;width:1200px;height:232px;background:var(--green-foot);color:var(--white)}
.foot-brand{left:40px;top:60px;width:160px;display:flex;flex-direction:column;align-items:center;gap:10px}
.foot-brand .brand-dot{width:52px;height:52px;background:var(--white)}
.foot-brand .brand-name{color:var(--white);font-size:19px;letter-spacing:4px}
.col h3{font-size:16px;font-weight:600;margin-bottom:15px}
.col ul{list-style:none}
.col li{font-size:13px;line-height:26px;padding-left:22px;position:relative}
.col li::before{content:"";position:absolute;left:3px;top:11px;width:5px;height:5px;border-radius:50%;background:var(--white)}
.social li{font-size:14px;line-height:28px;display:flex;align-items:center;gap:12px;padding-left:0}
.social li::before{display:none}
.social .sq{width:19px;height:19px;background:var(--white);display:inline-block}
.bottombar{left:0;top:1117px;width:1200px;height:46px;background:var(--green-dark);color:var(--white);font-size:12px;text-align:center;line-height:46px}
.bottombar .code{position:absolute;right:14px;top:0;font-size:14px}
</style>
</head>
<body>

<aside class="abs sidebar">
  <div class="brand">
    <span class="brand-dot"></span>
    <span class="brand-name">VENLOTRIX</span>
  </div>
  <ul class="menu">
    <li class="active"><svg width="14" height="16" viewBox="0 0 14 16"><circle cx="7" cy="4.5" r="4" fill="#e97a37"/><path d="M0 16c0-5 3-7 7-7s7 2 7 7z" fill="#e97a37"/></svg>Accounts</li>
    <li><svg width="18" height="16" viewBox="0 0 18 16"><path d="M0 8L18 0 14 16 9 11 16 3 7 10z" fill="#8f9496"/></svg>Send</li>
    <li><svg width="18" height="12" viewBox="0 0 18 12"><rect x="1" y="1" width="16" height="10" fill="none" stroke="#8f9496" stroke-width="2"/><circle cx="9" cy="6" r="2.5" fill="#8f9496"/></svg>Fund</li>
    <li><svg width="18" height="14" viewBox="0 0 18 14"><path d="M1 4h14M12 1l3 3-3 3M17 10H3M6 7l-3 3 3 3" fill="none" stroke="#8f9496" stroke-width="2"/></svg>Convert</li>
    <li><svg width="16" height="16" viewBox="0 0 16 16"><path d="M3 8a5 5 0 1 0 1.5-3.5" fill="none" stroke="#8f9496" stroke-width="2"/><path d="M1 2v5h5z" fill="#8f9496"/><path d="M8 5v3l2 2" fill="none" stroke="#8f9496" stroke-width="1.6"/></svg>History</li>
    <li><svg width="16" height="16" viewBox="0 0 16 16"><circle cx="8" cy="8" r="5" fill="none" stroke="#8f9496" stroke-width="4" stroke-dasharray="3 2"/><circle cx="8" cy="8" r="3" fill="#8f9496"/></svg>Settings</li>
  </ul>
</aside>

<header class="abs topbar">
  <span class="abs email">name @email.com</span>
  <div class="abs balance">US$11,051.09
    <span class="caret"><svg width="10" height="6" viewBox="0 0 10 6"><path d="M1 1l4 4 4-4" fill="none" stroke="#fff" stroke-width="1.8"/></svg></span>
  </div>
  <a class="abs nav" style="left:418px">My Wallet</a>
  <a class="abs nav" style="left:509px">Store</a>
  <a class="abs nav" style="left:573px">Explorer</a>
  <a class="abs nav" style="left:655px">About</a>
  <a class="abs nav" style="left:723px">Status</a>
  <a class="abs signout"><svg width="14" height="12" viewBox="0 0 14 12"><path d="M5 1H1v10h4" fill="none" stroke="#fff" stroke-width="2"/><path d="M5 6h6M9 3l3 3-3 3" fill="none" stroke="#fff" stroke-width="2"/></svg>Signout</a>
</header>

<div class="abs titlebar">
  <h1>Add Account</h1>
  <span class="abs help">?</span>
</div>

<!-- step 1 -->
<div class="abs step-num" style="left:320px;top:163px">1</div>
<h2 class="abs step-title" style="left:366px;top:170px">Choose a Custodian Custodians</h2>
<p class="abs copy" style="left:366px;top:216px;width:283px"><u>Custodians</u> hold assets on your behalf, You are trusting them with your monexLorem ipsum dolor sit amet, consectetur adipiscing elit. Nam et sodales tortor. Phasellus convallis elit est, placerat cursus magna dignissim facili-sis</p>
<div class="abs panel" style="left:366px;top:342px;width:280px;height:128px">
  <div class="option-bar">Pegmint</div>
  <div class="options">Ardent Vault Reserve<br>Solid Ledgerworks</div>
</div>
<div class="abs panel copy info" style="left:677px;top:175px;width:463px;height:295px">
  <p><u>Pegmint</u> currencies ore new assets that move on the Blockchain just as easily as bilcan. Pegmint currencies are essentially Dolor, Euros, and Yen formatted to work on the Blocks... Pegmints OIWOYS now Meir value e 11 to tile underlying asset.</p>
  <p style="margin-top:21px">Every Pegmint in circulation is backed 1:1 with a matching curr.cy in our customer reserve account and can be red.med at any time for its original asset, TNe means that for every USM', EURM, and JPM7 in a customs, wallet, we hold a real Dolor, Euro, or Y.. our bank account as a do. by the Pegmint holder</p>
</div>

<!-- step 2 -->
<div class="abs step-num" style="left:320px;top:515px">1</div>
<h2 class="abs step-title" style="left:366px;top:522px">Choose an Asset</h2>
<div class="abs panel options" style="left:366px;top:564px;width:280px;height:108px">USDM<br>EURM<br>JPYM</div>
<div class="abs panel copy info" style="left:677px;top:531px;width:463px;height:142px">
  <p>Classic US Dolor Pegmints. Issued using the Master.. protocol Com-patible with your Dubrapurse wallet, a. redeemable with popular services like <u>Tradelyn </u></p>
</div>

<!-- step 3 -->
<div class="abs step-num" style="left:320px;top:710px">3</div>
<h2 class="abs step-title" style="left:366px;top:717px">Terms of speach</h2>
<span class="abs check" style="left:367px;top:759px"></span>
<span class="abs copy" style="left:399px;top:756px;font-size:13.5px">I agree from now on that US Dollars, $, USD and US$ are all understood to mean USDM.</span>
<a class="abs btn" style="left:367px;top:802px;width:151px;height:40px">Add Account</a>

<footer class="abs footer">
  <div class="abs foot-brand">
    <span class="brand-dot"></span>
    <span class="brand-name">VENLOTRIX</span>
  </div>
  <div class="abs col" style="left:289px;top:24px">
    <h3>USEFUL LINKS</h3>
    <ul><li>Accounts</li><li>Send</li><li>Fund</li><li>Convert</li><li>History</li><li>Settings</li></ul>
  </div>
  <div class="abs col" style="left:530px;top:24px">
    <h3>MERCHANT SERVICES</h3>
    <ul><li>Information</li><li>Send Invoices</li><li>API</li></ul>
  </div>
  <div class="abs col" style="left:806px;top:24px">
    <h3>VENLOTRIX</h3>
    <ul><li>About Venlotrix</li><li>Blog</li><li>Contact</li><li>Support</li></ul>
  </div>
  <div class="abs col social" style="left:1056px;top:24px">
    <h3>FOLLOW US</h3>
    <ul>
      <li><span class="sq"></span>Friendly</li>
      <li><span class="sq"></span>Chirper</li>
      <li><span class="sq"></span>Worknet</li>
      <li><span class="sq"></span>Codehub</li>
      <li><span class="sq"></span>Longread</li>
    </ul>
  </div>
</footer>
<div class="abs bottombar">© 2012-2015 VENLOTRIX.COM | ALL RIGHTS RESERVED | PRIVACY POLICY | TERMS<span class="code">M3</span></div>

</body>
</html>
```